High-end residential home builder needs a business card design

We need a new business card design for a small residential construction company based in Boise, Idaho. We specialize in building custom high-end homes and remodels, with a focus on great design and craftsmanship.

We would like to use our current logo, but open to new color suggestions.
Just looking for a clean, sharp, modern design that looks high-end.

Target Market(s)

Upscale clientele

Industry/Entity Type

Contractor

Contact Information for Business Card

Company: Stonefield Custom Builders
Name: Marcus Tilley
Phone number: 208 367 4120
Email: MarcusTilleySCB@mailbox-example.com
Website: Stonefieldcustombuilders-example.com

Font styles to use
Serif
Sans Serif

Requirements
Must have
• Company Logo
Company name
My name
My phone number
My email
Company website
Nice to have
• I have attached a few photos of cards that I really like.

```html
<!DOCTYPE html>
<html lang="en">
<head>
<meta charset="utf-8">
<title>Stonefield Custom Builders – Business Card</title>
<link rel="stylesheet" href="https://fonts.googleapis.com/css2?family=Montserrat:wght@400;500;700&display=swap">
<style>
  :root {
    --backdrop: #e6eef3;
    --card: #ffffff;
    --ink: #1e1414;
    --accent: #e88a1c;
  }
  * { box-sizing: border-box; margin: 0; padding: 0; }
  html, body {
    width: 1200px; height: 1200px; overflow: hidden;
    background: var(--backdrop);
    font-family: "Montserrat", Arial, sans-serif;
    color: var(--ink);
  }
  .card {
    position: absolute;
    left: 180px;
    width: 840px; height: 480px;
    background: var(--card);
  }
  .card--front { top: 99px; }
  .card--back { top: 630px; }

  /* Front */
  .brand {
    position: absolute; left: 0; right: 0; top: 168px;
    text-align: center;
  }
  .brand__mark {
    display: block; margin: 0 auto 26px;
    width: 22px; height: 22px; background: var(--accent);
  }
  .brand__name {
    font-weight: 500; font-size: 24px;
    letter-spacing: 0.32em; line-height: 1.7;
    padding-left: 0.32em;
    text-transform: uppercase;
  }

  /* Back */
  .badge {
    position: absolute; left: 73px; top: 84px;
    display: flex; align-items: center; gap: 10px;
  }
  .badge__mark { width: 14px; height: 14px; background: var(--accent); }
  .badge__name {
    font-weight: 500; font-size: 13px; letter-spacing: 0.28em;
    text-transform: uppercase;
  }
  .holder {
    position: absolute; left: 0; right: 0; top: 168px;
    text-align: center;
    font-size: 44px; letter-spacing: 0.3em; padding-left: 0.3em;
    text-transform: uppercase; line-height: 1;
  }
  .holder__first { font-weight: 400; }
  .holder__last { font-weight: 700; }
  .divider {
    position: absolute; top: 249px; left: 335px;
    width: 170px; height: 2px; background: var(--ink);
  }
  .contact {
    position: absolute; left: 0; right: 0; top: 307px;
    text-align: center; font-size: 12px; line-height: 1;
  }
  .contact p { margin-bottom: 16px; }
  .contact__gap { display: inline-block; width: 16px; }
</style>
</head>
<body>
  <section class="card card--front">
    <div class="brand">
      <span class="brand__mark"></span>
      <p class="brand__name">Stonefield<br>Custom Builders</p>
    </div>
  </section>

  <section class="card card--back">
    <div class="badge">
      <span class="badge__mark"></span>
      <span class="badge__name">Stonefield</span>
    </div>
    <h1 class="holder"><span class="holder__first">Marcus</span> <span class="holder__last">Tilley</span></h1>
    <div class="divider"></div>
    <div class="contact">
      <p>Stonefield Custom Builders</p>
      <p>Phone&nbsp; 208 367 4120<span class="contact__gap"></span>MarcusTilleySCB@mailbox-example.com</p>
      <p>www.Stonefieldcustombuilders-example.com</p>
    </div>
  </section>
</body>
</html>
```